Premium men's gut health supplement needs a bottle label designed

We’re velnora - a premium men’s wellness brand focused on gut health. Our first product is a high-quality daily supplement designed to support digestion, regularity, and internal cleanliness. Backed by science and tailored for modern lifestyles, velnora is crafted in the UK and proudly LGBT-owned. It aims to resolve intimacy problems that gay men may experience due to poor digestion but also does not exclude any other orientation - other men may use it simply to improve their digestion.

velnora is for health-conscious men who value science-backed supplements and want to feel confident from the inside out. Many of our early adopters will be gay and bisexual men who prioritise gut health as part of their self-care, sexual, and hygiene routine, though the product is equally effective and appealing to anyone seeking premium digestive support.

The product is premium the target customer is male, not specific to one location but primary markets will be US, UK and EU.

I’d like a supplement bottle designed for velnora, our premium men’s gut health brand. The focus should be clean, slightly clinical, and minimal - inspired by brands like Quelrin and Darvo. The key element is the wordmark (velnora) on the front, with no additional logo or icon. Lowercase text and a strong, contemporary font are preferred.

The bottle should be aesthetically pleasing so that people are proud to display it on their shelf, instead of hiding it in a cupboard (like Quelrin, darvo, Pia Venturek, Morvanel etc)

Avoid anything that shows the product as being for LGBT, e.g., no rainbows, men holding hands etc.

The design should be premium, minimalist and not be busy or overwhelming.

I have uploaded a file called "Bottle" to give an idea of the type of container, but please ignore the colours and change as you see fit. This is just for reference for the type of bottle we'll use - all colours are customisable.

I have also uploaded some images for "style" reference, e.g., darvo, quelrin, pia venturek, etc for inspiration.

```html
<!DOCTYPE html>
<html lang="en">
<head>
<meta charset="utf-8">
<title>velnora — men's gut health supplement label</title>
<link rel="stylesheet" href="https://fonts.googleapis.com/css2?family=Figtree:wght@300;400;600;800&display=swap">
<style>
  :root {
    --page-bg: #f4f4f4;
    --label-white: #ffffff;
    --label-edge: #e6e6e6;
    --ink: #0d0d0d;
    --brand-orange: #e9501f;
    --orange-deep: #e53d1c;
    --orange-warm: #f7963a;
    --orange-rust: #cf4a1c;
    --on-orange: #ffffff;
  }
  * { margin: 0; padding: 0; box-sizing: border-box; }
  html, body {
    width: 1200px;
    height: 959px;
    overflow: hidden;
    background: var(--page-bg);
    font-family: "Figtree", sans-serif;
  }
  .presentation {
    position: relative;
    width: 1200px;
    height: 959px;
    overflow: hidden;
  }
  .brand-wordmark {
    position: absolute;
    left: 0;
    width: 100%;
    top: 78px;
    text-align: center;
    font-size: 84px;
    font-weight: 800;
    letter-spacing: -2px;
    color: var(--brand-orange);
    line-height: 1;
  }
  .label {
    position: absolute;
    top: 449px;
    width: 311px;
    height: 401px;
    border-radius: 14px;
    overflow: hidden;
    box-shadow: 0 0 0 1px var(--label-edge);
  }
  .label--first { left: 190px; }
  .label--second { left: 603px; }
  .label--third { left: 1034px; }
  .label__head {
    height: 133px;
    background: var(--label-white);
    display: flex;
    align-items: center;
    justify-content: center;
  }
  .label__wordmark {
    font-size: 70px;
    font-weight: 800;
    letter-spacing: -2px;
    color: var(--ink);
    line-height: 1;
    margin-top: 10px;
  }
  .label__body {
    position: relative;
    height: 268px;
    color: var(--on-orange);
    background:
      radial-gradient(circle at 100% 0%, rgba(240,150,60,0.55), transparent 45%),
      radial-gradient(circle at 0% 100%, var(--orange-warm), transparent 55%),
      linear-gradient(160deg, var(--orange-deep) 0%, #ec6424 45%, var(--orange-rust) 100%);
  }
  .label__type {
    position: absolute;
    top: 34px;
    left: 0;
    width: 100%;
    text-align: center;
    font-size: 25px;
    line-height: 33px;
  }
  .label__type-line--light { font-weight: 300; display: block; }
  .label__type-line--bold { font-weight: 600; display: block; }
  .benefit {
    position: absolute;
    height: 34px;
    border: 1.3px solid var(--on-orange);
    border-radius: 17px;
    font-size: 16.5px;
    font-weight: 400;
    display: flex;
    align-items: center;
    justify-content: center;
    white-space: nowrap;
  }
  .benefit--digestion { left: 20px; top: 116px; width: 156px; }
  .benefit--clarity { left: 85px; top: 163px; width: 154px; }
  .benefit-plus {
    position: absolute;
    left: 119px;
    top: 144px;
    width: 22px;
    height: 22px;
  }
  .label__count {
    position: absolute;
    left: 0;
    width: 100%;
    bottom: 18px;
    text-align: center;
    font-size: 18px;
    font-weight: 400;
  }
</style>
</head>
<body>
<main class="presentation">
  <h1 class="brand-wordmark">velnora</h1>

  <section class="label label--first">
    <div class="label__head"><span class="label__wordmark">velnora</span></div>
    <div class="label__body">
      <p class="label__type">
        <span class="label__type-line--light">men’s gut</span>
        <span class="label__type-line--bold">health supplement</span>
      </p>
      <span class="benefit benefit--digestion">daily digestion</span>
      <svg class="benefit-plus" viewBox="0 0 22 22" aria-hidden="true"><path d="M11 2v18M2 11h18" stroke="#fff" stroke-width="1.6"/></svg>
      <span class="benefit benefit--clarity">internal clarity</span>
      <p class="label__count">30 capsules</p>
    </div>
  </section>

  <section class="label label--second">
    <div class="label__head"><span class="label__wordmark">velnora</span></div>
    <div class="label__body">
      <p class="label__type">
        <span class="label__type-line--light">men’s gut</span>
        <span class="label__type-line--bold">health supplement</span>
      </p>
      <span class="benefit benefit--digestion">daily digestion</span>
      <svg class="benefit-plus" viewBox="0 0 22 22" aria-hidden="true"><path d="M11 2v18M2 11h18" stroke="#fff" stroke-width="1.6"/></svg>
      <span class="benefit benefit--clarity">internal clarity</span>
      <p class="label__count">30 capsules</p>
    </div>
  </section>

  <section class="label label--third">
    <div class="label__head"><span class="label__wordmark">velnora</span></div>
    <div class="label__body">
      <p class="label__type">
        <span class="label__type-line--light">men’s gut</span>
        <span class="label__type-line--bold">health supplement</span>
      </p>
      <span class="benefit benefit--digestion">daily digestion</span>
      <svg class="benefit-plus" viewBox="0 0 22 22" aria-hidden="true"><path d="M11 2v18M2 11h18" stroke="#fff" stroke-width="1.6"/></svg>
      <span class="benefit benefit--clarity">internal clarity</span>
      <p class="label__count">30 capsules</p>
    </div>
  </section>
</main>
</body>
</html>
```